Global Beard Oil Review Business needs a refresh

topwhiskertonic.net is a global business who's mission is to curate all available beard oils from around the world, review and grade them and present this curated collection to the user of the website.

The scope of this job includes the web site design and the design of a suitable logo to be used in the site header.

The existing site can be seen on http://topwhiskertonic.net, however this is a mock-up only the style and logo should NOT be used. This is to give you an idea of the concept of the site only.

This job is for PSD design only.

See attached design brief for detailed design requirements.
Updates

Project Deadline Extended
Reason: Extending deadline by 5 days to allow for final submissions

Target Market(s)

Men's grooming / retail

Industry/Entity Type

Retail

Number of Pages Required

2 page

Font styles to use
Sans Serif

Requirements
Must have
• 1) Comparison Table
• 2) Side Bar
• 3) Header area
• 4) Photo of Calvin Dorrow (attached - can be circular or "cut-out")
• 5) Cool beard-oriented custom design background (e.g., stylistic black/brown on brown/orange beard background. I envision this beard background "drawing" rather than photo based)
• (see attached design requirements for details)
Nice to have
• Signature style writing at top with name "Calvin Dorrow"
Should not have
• Do NOT use the look & feel or logo from the existing site.

```html
<!DOCTYPE html>
<html lang="en">
<head>
<meta charset="utf-8">
<title>Top Whisker Tonic – Beard Oil Reviews</title>
<link href="https://fonts.googleapis.com/css2?family=Lato:ital,wght@0,400;0,700;0,900;1,400&family=Dancing+Script:wght@500&display=swap" rel="stylesheet">
<style>
:root{
  --orange:#f7941d;
  --orange-dark:#e07f0c;
  --wood-dark:#3b3b3b;
  --wood-mid:#8d8d8d;
  --wood-foot:#2f2f2f;
  --panel:#cfcfcf;
  --side:#3e3e3e;
  --ink:#333;
  --ink-soft:#555;
  --pip-off:#e6e6e6;
  --pip-on:#4a4a4a;
  --white:#fff;
  --black:#080808;
}
*{box-sizing:border-box;margin:0;padding:0}
html,body{width:1200px;height:945px;overflow:hidden}
body{font-family:"Lato",sans-serif;color:var(--ink);background:var(--wood-dark)}
.canvas{position:relative;width:1200px;height:945px;overflow:hidden}
.band{position:absolute;left:0;width:1200px}
.band--header{top:0;height:222px;background:linear-gradient(180deg,#414141,#333)}
.band--main{top:222px;height:454px;background:linear-gradient(180deg,#949494,#7f7f7f)}
.band--footer{top:676px;height:129px;background:var(--wood-foot)}
.band--legal{top:805px;height:27px;background:var(--black)}
.band--base{top:832px;height:113px;background:linear-gradient(180deg,#454545,#393939)}

.brand{position:absolute;left:0;width:1200px;top:52px;display:flex;justify-content:center;align-items:center;gap:12px}
.brand__dot{width:44px;height:44px;border-radius:50%;background:var(--orange)}
.brand__name{font:900 34px "Lato",sans-serif;color:var(--orange);letter-spacing:.5px}

.nav{position:absolute;top:180px;left:0;width:1200px;height:42px}
.nav a{position:absolute;top:0;font:700 18px "Lato",sans-serif;font-variant:small-caps;color:var(--white);text-decoration:none;text-shadow:0 1px 2px rgba(0,0,0,.6)}
.nav a.is-active,.nav a.is-hover{color:var(--orange)}
.nav a.is-active::after{content:"";position:absolute;left:0;right:0;top:39px;height:2px;background:var(--orange)}

.panel{position:absolute;left:160px;top:237px;width:691px;height:425px;background:var(--panel)}
.panel__title{position:absolute;left:13px;top:20px;font:700 20px "Lato",sans-serif;font-variant:small-caps;color:var(--ink)}
.panel__intro{position:absolute;left:13px;top:48px;width:540px;font-size:9px;line-height:17px;color:var(--ink)}
.author{position:absolute;left:572px;top:20px;width:120px;text-align:center}
.author__photo{display:block;width:88px;height:88px;margin:0 auto;border-radius:50%;background:radial-gradient(circle at 50% 40%,#6a6a6a,#1f1f1f)}
.author__role{margin-top:8px;font:700 10px "Lato",sans-serif;color:var(--ink)}
.author__sign{margin-top:2px;font:500 12px "Dancing Script",cursive;color:var(--ink-soft)}
.scale{position:absolute;left:75px;top:124px;display:flex;align-items:center;gap:8px}
.scale__note{font:500 11px "Dancing Script",cursive;color:var(--ink-soft);transform:rotate(-3deg)}
.scale__pips{display:flex;gap:8px}
.scale__pips span{width:24px;height:24px;border-radius:50%;background:var(--orange)}
.scale__pips span.off{background:#eee}

.chart{position:absolute;left:15px;top:177px;width:663px;border-collapse:collapse;table-layout:fixed}
.chart th{font:700 8px "Lato",sans-serif;font-variant:small-caps;text-align:left;color:var(--ink);height:14px;border-bottom:1px solid #777;padding:0 0 2px 3px}
.chart td{height:38.5px;font-size:8.5px;line-height:8.5px;color:var(--ink);padding-left:3px;vertical-align:middle}
.bottle{display:block;width:9px;height:24px;border-radius:3px 3px 2px 2px;background:linear-gradient(180deg,#222 0 25%,#5b3b1a 25%)}
.bottle--clear{background:linear-gradient(180deg,#777 0 25%,#b9925f 25%)}
.pips{display:flex;gap:3.5px}
.pip{width:9px;height:9px;border-radius:50%;background:var(--pip-off)}
.pip.on{background:var(--pip-on)}
.pips--overall .pip.on{background:var(--orange)}
.cta{display:inline-block;width:57px;height:16px;border-radius:8px;background:var(--orange);color:var(--white);font:700 5px/16px "Lato",sans-serif;text-align:center;box-shadow:0 1px 2px rgba(0,0,0,.3)}
.more{position:absolute;left:319px;top:397px;width:55px;height:19px;background:#7a7a7a;color:var(--white);font-size:6px;line-height:19px;text-align:center}

.sidebar{position:absolute;left:866px;top:237px;width:172px;height:425px;background:var(--side)}
.sidebar__head{position:absolute;left:8px;width:157px;height:16px;display:flex;align-items:center;gap:5px;border-bottom:1px solid #ddd;color:var(--white);font:700 10px "Lato",sans-serif}
.sidebar__icon{width:15px;height:15px;background:var(--orange)}
.sidebar__icon--round{border-radius:50%}
.entry{position:absolute;left:7px;width:158px;height:58px}
.entry+.entry{border-top:1px solid #666}
.entry__thumb{position:absolute;left:0;top:0;width:47px;height:49px}
.entry__body{position:absolute;left:52px;top:0;width:108px;color:var(--white)}
.entry__title{font:900 7.5px/10px "Lato",sans-serif;text-transform:uppercase}
.entry__meta{font-size:7.5px;line-height:13px;color:#ddd}
.entry__meta b{font-weight:400;color:var(--orange)}
.entry__text{font-size:7.5px;line-height:10.5px;color:#bbb;margin-top:2px}

.foot-col{position:absolute;top:695px;color:var(--white)}
.foot-col h3{font:700 12px "Lato",sans-serif;font-variant:small-caps;text-decoration:underline;text-underline-offset:2px;margin-bottom:6px}
.links{list-style:none;font-size:9px;line-height:13.6px}
.newsletter p{font-size:8.5px;line-height:10.5px;width:110px}
.newsletter__input{margin-top:5px;width:125px;height:18px;border:1px solid #ccc;background:transparent;color:#bbb;font-size:8px;line-height:16px;padding-left:6px}
.newsletter__btn{margin-top:9px;width:57px;height:18px;background:var(--orange);color:var(--white);font:700 6px/18px "Lato",sans-serif;text-align:center}
.tags{display:flex;flex-wrap:wrap;gap:4px;width:140px}
.tag{height:19px;padding:0 3px;background:var(--orange);font-size:8.5px;line-height:19px;color:var(--white)}
.social{display:flex;gap:8px;margin-top:-1px}
.social span{width:18px;height:18px;background:var(--orange);border-radius:2px}
.legal{position:absolute;left:162px;top:813px;font:700 8.5px "Lato",sans-serif;color:var(--white)}
.legal i{font-weight:700}
</style>
</head>
<body>
<div class="canvas">
  <div class="band band--header" role="img" aria-label="Dark weathered wood plank background"></div>
  <div class="band band--main" role="img" aria-label="Grey wood plank background"></div>
  <div class="band band--footer"></div>
  <div class="band band--legal"></div>
  <div class="band band--base" role="img" aria-label="Dark wood plank background"></div>

  <header>
    <div class="brand"><span class="brand__dot"></span><span class="brand__name">Top Whisker Tonic</span></div>
    <nav class="nav">
      <a class="is-active" href="#" style="left:328px">Home</a>
      <a href="#" style="left:415px">Review Methodology</a>
      <a class="is-hover" href="#" style="left:613px">Charter</a>
      <a href="#" style="left:718px">Blog</a>
      <a href="#" style="left:799px">About Me</a>
    </nav>
  </header>

  <main class="panel">
    <h1 class="panel__title">The World's #1 Beard Oil Authority</h1>
    <p class="panel__intro">Here is the master list of beard oils reviewed to date and ranked on our unic <i>"beard scale"</i>. You can link directly to the corresponding review by clicking on the name of the beard oil. In accordance with our charter, we are actively working to locate and review every single beard oil available on the planet Earth, so check back regularly for updates.</p>
    <div class="author">
      <span class="author__photo" role="img" aria-label="Portrait photo of Calvin Dorrow"></span>
      <p class="author__role">Global Beard Oil Reviews</p>
      <p class="author__sign">- by Calvin Dorrow</p>
    </div>
    <div class="scale">
      <span class="scale__note">Introducing our new "beard scale" rating system &rarr;</span>
      <span class="scale__pips"><span></span><span></span><span></span><span></span><span class="off"></span></span>
    </div>

    <table class="chart">
      <colgroup><col style="width:53px"><col style="width:66px"><col style="width:28px"><col style="width:40px"><col style="width:46px"><col style="width:66px"><col style="width:75px"><col style="width:75px"><col style="width:76px"><col style="width:78px"><col style="width:60px"></colgroup>
      <thead><tr><th>Suplier</th><th>Name</th><th>Oil</th><th>Origin</th><th>Base Oil</th><th>Scent</th><th>Aroma</th><th>Therapeutic Affect</th><th>Value</th><th>Overall</th><th>Link</th></tr></thead>
      <tbody>
        <tr><td>Northfold Beard Co.</td><td>Timberhand</td><td><span class="bottle" role="img" aria-label="Bottle photo"></span></td><td>AU</td><td>Almond</td><td>Tea Tree</td>
          <td><span class="pips"><i class="pip on"></i><i class="pip on"></i><i class="pip on"></i><i class="pip on"></i><i class="pip on"></i></span></td>
          <td><span class="pips"><i class="pip on"></i><i class="pip on"></i><i class="pip on"></i><i class="pip on"></i><i class="pip"></i></span></td>
          <td><span class="pips"><i class="pip on"></i><i class="pip on"></i><i class="pip on"></i><i class="pip on"></i><i class="pip on"></i></span></td>
          <td><span class="pips pips--overall"><i class="pip on"></i><i class="pip on"></i><i class="pip on"></i><i class="pip on"></i><i class="pip"></i></span></td>
          <td><span class="cta">GET YOURS NOW</span></td></tr>
        <tr><td>Papa Rigs Grooming</td><td>Hazy Ridge Man Beard Oil</td><td><span class="bottle" role="img" aria-label="Bottle photo"></span></td><td>AU</td><td>Castor</td><td>Pinewood</td>
          <td><span class="pips"><i class="pip on"></i><i class="pip on"></i><i class="pip on"></i><i class="pip on"></i><i class="pip"></i></span></td>
          <td><span class="pips"><i class="pip on"></i><i class="pip on"></i><i class="pip on"></i><i class="pip"></i><i class="pip"></i></span></td>
          <td><span class="pips"><i class="pip on"></i><i class="pip on"></i><i class="pip on"></i><i class="pip on"></i><i class="pip on"></i></span></td>
          <td><span class="pips pips--overall"><i class="pip on"></i><i class="pip on"></i><i class="pip on"></i><i class="pip"></i><i class="pip"></i></span></td>
          <td><span class="cta">GET YOURS NOW</span></td></tr>
        <tr><td>Bristled Rogue</td><td>Pinewright</td><td><span class="bottle bottle--clear" role="img" aria-label="Bottle photo"></span></td><td>USA</td><td>Coconut</td><td>Fir Needle</td>
          <td><span class="pips"><i class="pip on"></i><i class="pip on"></i><i class="pip on"></i><i class="pip on"></i><i class="pip on"></i></span></td>
          <td><span class="pips"><i class="pip on"></i><i class="pip on"></i><i class="pip on"></i><i class="pip on"></i><i class="pip"></i></span></td>
          <td><span class="pips"><i class="pip on"></i><i class="pip on"></i><i class="pip on"></i><i class="pip on"></i><i class="pip on"></i></span></td>
          <td><span class="pips pips--overall"><i class="pip on"></i><i class="pip on"></i><i class="pip on"></i><i class="pip on"></i><i class="pip"></i></span></td>
          <td><span class="cta">GET YOURS NOW</span></td></tr>
        <tr><td>Chopmark Men's Grooming</td><td>Chopmark Beard Oil</td><td><span class="bottle" role="img" aria-label="Bottle photo"></span></td><td>AU</td><td>Vitamine E</td><td>Cedarwood</td>
          <td><span class="pips"><i class="pip on"></i><i class="pip on"></i><i class="pip on"></i><i class="pip"></i><i class="pip"></i></span></td>
          <td><span class="pips"><i class="pip on"></i><i class="pip on"></i><i class="pip on"></i><i class="pip on"></i><i class="pip on"></i></span></td>
          <td><span class="pips"><i class="pip on"></i><i class="pip on"></i><i class="pip on"></i><i class="pip on"></i><i class="pip"></i></span></td>
          <td><span class="pips pips--overall"><i class="pip on"></i><i class="pip on"></i><i class="pip on"></i><i class="pip"></i><i class="pip"></i></span></td>
          <td><span class="cta">GET YOURS NOW</span></td></tr>
        <tr><td>Evenwell Soaps</td><td>Outbacker's Beard Oil</td><td><span class="bottle" role="img" aria-label="Bottle photo"></span></td><td>AU</td><td>Almond</td><td>Sandalwood</td>
          <td><span class="pips"><i class="pip on"></i><i class="pip on"></i><i class="pip on"></i><i class="pip on"></i><i class="pip"></i></span></td>
          <td><span class="pips"><i class="pip on"></i><i class="pip on"></i><i class="pip on"></i><i class="pip"></i><i class="pip"></i></span></td>
          <td><span class="pips"><i class="pip on"></i><i class="pip on"></i><i class="pip on"></i><i class="pip on"></i><i class="pip on"></i></span></td>
          <td><span class="pips pips--overall"><i class="pip on"></i><i class="pip on"></i><i class="pip on"></i><i class="pip"></i><i class="pip"></i></span></td>
          <td><span class="cta">GET YOURS NOW</span></td></tr>
      </tbody>
    </table>
    <span class="more">View more ...</span>
  </main>

  <aside class="sidebar">
    <h2 class="sidebar__head" style="top:10px"><span class="sidebar__icon"></span>Popular Posts</h2>
    <article class="entry" style="top:38px">
      <span class="entry__thumb" role="img" aria-label="Photo of a leather pouch" style="background:linear-gradient(160deg,#b57a3a,#6b4520)"></span>
      <div class="entry__body"><p class="entry__title">Hazy Ridge Man Beard Oil Papa ...</p><p class="entry__meta">BY: <b>Calvin Dorrow</b></p><p class="entry__meta">February 12, 2016</p></div>
    </article>
    <article class="entry" style="top:96px">
      <span class="entry__thumb" role="img" aria-label="Photo of a bottle outdoors" style="background:linear-gradient(160deg,#8a9a6a,#3d4a2c)"></span>
      <div class="entry__body" style="top:4px"><p class="entry__title">Outbacker's Face/Beard Oil by Evenwell ...</p><p class="entry__meta">BY: <b>Calvin Dorrow</b></p><p class="entry__meta">February 09, 2016</p></div>
    </article>
    <article class="entry" style="top:154px">
      <span class="entry__thumb" role="img" aria-label="Photo of a beard oil pouch" style="background:linear-gradient(160deg,#c9bb8e,#7d6e45)"></span>
      <div class="entry__body" style="top:4px"><p class="entry__title">Chopmark Beard Oil by Chopmark ...</p><p class="entry__meta">BY: <b>Calvin Dorrow</b></p><p class="entry__meta">January 25, 2016</p></div>
    </article>

    <h2 class="sidebar__head" style="top:223px"><span class="sidebar__icon sidebar__icon--round"></span>Recent Comments</h2>
    <article class="entry" style="top:257px">
      <span class="entry__thumb" role="img" aria-label="Commenter profile photo" style="background:linear-gradient(160deg,#9a8a78,#4a3f35)"></span>
      <div class="entry__body"><p class="entry__title">Phil</p><p class="entry__text">Great reviews, really helpful ! My beard and I thank you lol</p></div>
    </article>
    <article class="entry" style="top:315px">
      <span class="entry__thumb" role="img" aria-label="Commenter profile photo" style="background:linear-gradient(160deg,#7a8088,#35393d)"></span>
      <div class="entry__body" style="top:4px"><p class="entry__title">James</p><p class="entry__text">My grandfather used this oil, he swore be it</p></div>
    </article>
    <article class="entry" style="top:373px">
      <span class="entry__thumb" role="img" aria-label="Commenter profile photo" style="background:linear-gradient(160deg,#c7a58a,#8a2f2a)"></span>
      <div class="entry__body" style="top:4px"><p class="entry__title">Robert</p><p class="entry__text">The misusus loved this oil on my beard !!</p></div>
    </article>
  </aside>

  <footer>
    <section class="foot-col" style="left:161px">
      <h3>Quick Links</h3>
      <ul class="links"><li>Home</li><li>Review Methedology</li><li>Charter</li><li>Blog</li><li>About Me</li><li>Contact</li></ul>
    </section>
    <section class="foot-col newsletter" style="left:406px">
      <h3>Subscribe to my newsletter</h3>
      <p>Don't miss out on any of my reviews and offers.</p>
      <div class="newsletter__input">Enter your email here</div>
      <div class="newsletter__btn">SUBMIT</div>
    </section>
    <section class="foot-col" style="left:677px">
      <h3>Tags</h3>
      <div class="tags"><span class="tag">Refreshing</span><span class="tag">Afordable</span><span class="tag">Cooling</span><span class="tag">Comfortable</span><span class="tag">Awesome</span><span class="tag">Oilly</span></div>
    </section>
    <section class="foot-col" style="left:972px;top:691px">
      <h3>Follow me on</h3>
      <div class="social"><span></span><span></span><span></span></div>
    </section>
    <p class="legal">Copyright @ 2016 <i>Top Whisker Tonic</i> -&nbsp; All rights reserved</p>
  </footer>
</div>
</body>
</html>
```